Flyer required for podiatry clinic

DL Size please.
Wanting a design for a mail box flyer for the local area. Wanting to increase our customer base. The information on the attached word document needs to be included.
If stock photos are able to be fit in that would be appreciated
We cater from young children to the elderly so should be suitable for all.

Colors

Designer to choose colors to be used in the design.

```html
<!DOCTYPE html>
<html lang="en">
<head>
<meta charset="utf-8">
<title>Stridewell Podiatry – Flyer</title>
<link rel="stylesheet" href="https://fonts.googleapis.com/css2?family=Fira+Sans:wght@400;600;700&family=Nunito:wght@800&display=swap">
<style>
  :root{
    --page:#f2f2f2;
    --green:#9bbf3b;
    --navy:#0f4f73;
    --sky:#3791b8;
    --teal:#2a86a6;
    --white:#ffffff;
    --sand-1:#f6e7c8;
    --sand-2:#e9c995;
    --skin-1:#f4d3c2;
    --skin-2:#e8ad98;
  }
  *{margin:0;padding:0;box-sizing:border-box}
  html,body{width:1200px;height:1200px;overflow:hidden;background:var(--page)}
  .flyer{position:absolute;left:345px;top:75px;width:510px;height:1050px;background:var(--green);overflow:hidden;font-family:"Fira Sans",sans-serif;color:var(--white)}
  .hero-photo{position:absolute;left:0;top:0;width:510px;height:420px;background:linear-gradient(180deg,#fbf3e4 0%,var(--sand-1) 45%,var(--sand-2) 100%)}
  .waves{position:absolute;left:0;top:0}
  .brand{position:absolute;left:26px;top:34px;font-family:"Nunito",sans-serif;font-weight:800;font-size:44px;line-height:42px;color:var(--teal);letter-spacing:-0.5px}
  .photo-circle{position:absolute;border-radius:50%;border:4px solid var(--navy);background:radial-gradient(circle at 45% 40%,var(--skin-1),var(--skin-2))}
  .photo-circle::after{content:"";position:absolute;inset:2px;border-radius:50%;border:3px solid var(--white)}
  .hero-circle{left:324px;top:272px;width:178px;height:178px}
  .thumb-1{left:16px;top:738px;width:108px;height:108px;background:radial-gradient(circle at 55% 45%,#f1dccf,#c9d6de)}
  .thumb-2{left:200px;top:722px;width:108px;height:108px}
  .thumb-3{left:387px;top:724px;width:108px;height:108px;background:radial-gradient(circle at 50% 55%,#f3c9b3,#f7f1ef)}
  .services{position:absolute;left:30px;top:452px;list-style:none;font-weight:600;font-size:19px;line-height:25.8px}
  .services li::before{content:"•";font-size:13px;margin-right:9px;vertical-align:2px}
  .billing{position:absolute;left:0;width:510px;top:666px;text-align:center;color:var(--navy);font-weight:700;font-size:18.5px;line-height:24.5px}
  .locations-title{position:absolute;left:154px;top:844px;width:201px;height:28px;background:var(--green);text-align:center;font-weight:700;font-size:20px;line-height:28px}
  .location{position:absolute;top:886px;width:164px;text-align:center;font-weight:700}
  .location h3{font-size:12.5px;line-height:16px;font-weight:700}
  .location p{font-size:10.5px;line-height:14.5px;font-weight:600}
  .location .phone{font-size:17px;line-height:24px;margin-top:2px}
  .loc-1{left:8px}.loc-2{left:172px}.loc-3{left:340px}
  .divider{position:absolute;top:888px;width:1.5px;height:80px;background:var(--green)}
  .div-1{left:174px}.div-2{left:341px}
  .footer{position:absolute;left:0;top:978px;width:510px;height:72px;background:var(--navy);text-align:center}
  .web{margin-top:9px;font-size:13.5px;font-weight:600;line-height:18px}
  .web svg{vertical-align:-2px;margin-right:6px}
  .team{font-size:14.5px;line-height:22px;font-weight:400}
</style>
</head>
<body>
<main class="flyer">
  <div class="hero-photo" role="img" aria-label="Family playing joyfully on a beach at sunset"></div>

  <svg class="waves" width="510" height="1050" viewBox="0 0 510 1050" aria-hidden="true">
    <path d="M0,378 C150,422 330,412 510,286 L510,338 C340,452 150,452 0,432 Z" fill="#0f4f73"/>
    <path d="M0,372 C150,416 330,406 510,280" fill="none" stroke="#ffffff" stroke-width="7"/>
    <path d="M0,798 C110,830 190,790 300,772 C400,756 450,778 510,752" fill="none" stroke="#ffffff" stroke-width="12"/>
    <path d="M0,808 C110,840 190,800 300,782 C400,766 450,788 510,762 L510,980 L0,980 Z" fill="#3791b8"/>
  </svg>

  <div class="brand">Stridewell<br>Podiatry</div>

  <div class="photo-circle hero-circle" role="img" aria-label="Hands massaging the sole of a foot"></div>

  <ul class="services">
    <li>Heel Pain- Spurs and Plantar Fasciitis</li>
    <li>Orthotics</li>
    <li>Fungal Nail Infections (Laser treatment)</li>
    <li>Diabetes Foot Assessments</li>
    <li>Foot and ankle pain</li>
    <li>Flat Feet- Both adults and children</li>
    <li>Ingrown nails</li>
    <li>Corns/Callus</li>
  </ul>

  <p class="billing">BULK BILLING for GP EPC/ Care plans , DVA Card<br>Holders.Health fund claims and EFTPOS available</p>

  <div class="photo-circle thumb-1" role="img" aria-label="Podiatrist treating a patient's foot"></div>
  <div class="photo-circle thumb-2" role="img" aria-label="Close-up of heels from behind"></div>
  <div class="photo-circle thumb-3" role="img" aria-label="Bare feet standing on tiptoe"></div>

  <div class="locations-title">3 Handy locations</div>

  <div class="location loc-1">
    <h3>Riverside Private<br>Medical Centre:</h3>
    <p>Level 1, 58 Banksia<br>Lane Millbrook</p>
    <p class="phone">Ph: 5550 1234</p>
  </div>
  <span class="divider div-1"></span>
  <div class="location loc-2">
    <h3>Millbrook<br>Rehabilitation:</h3>
    <p>14 Wattle Street<br>Millbrook</p>
    <p class="phone">Ph: 5550 2468</p>
  </div>
  <span class="divider div-2"></span>
  <div class="location loc-3">
    <h3>Parkside Health<br>Hub:</h3>
    <p>210 Banksia Lane<br>Millbrook</p>
    <p class="phone">Ph: 5550 3579</p>
  </div>

  <footer class="footer">
    <p class="web"><svg width="13" height="13" viewBox="0 0 14 14" aria-hidden="true"><g fill="none" stroke="#9bbf3b" stroke-width="1.3"><circle cx="7" cy="7" r="6"/><ellipse cx="7" cy="7" rx="2.6" ry="6"/><path d="M1,7H13M2,3.8H12M2,10.2H12"/></g></svg>www.stridewell-podiatry.com.au</p>
    <p class="team">Podiatrist Daniel Ashford, Leah Moreton, Clara Whitby</p>
  </footer>
</main>
</body>
</html>
```